Flyer Design for a Mediation (Rediation on Quiet Rivers)

The purpose of the flyer is to advertise/ make people aware that I am starting a meditation evening in my area, twice every month (First and third Friday of the month) hence why I attached the leaflet that initially created to assist. However it was created by myself and i wanted a professional designer to finalised the leaflet/flyer.

I would like a 2 sided leaflet.
Front of leaflet

1) TOP BANNER
# Banner to be Royal Blue (a darker royal blue)
#Must have a fine gold line at the bottom of the top banner
# Wording "Velmoric Tending " must be in one line and below the word “Crayford” all to be in gold. Please note that wording must be placed to the far left hand side.
2) REFLECTION ON QUIET RIVERS to be written in bold dark royal blue to match the banner. This is to be placed to the centre of the page.
Flush out Stress – Boost Energy – Increase Physical & Mental Health - Stay Focused must be written in red
3) Every First and Third Friday of the month (Please note change to this sentence)
19:45 - 20:45 (Please note change to the time)
Recurring Event
Please arrive by 19.30 for a brief introduction .

4) Our guided Mediation is for over 18’s only. Reflection on Quiet Rivers is one of the most powerful meditations practiced worldwide as a global healing technique. (the wording “Reflection on Quiet Rivers” in this sentence, must be in Gold)

5) The following details to be added to the first page:
Eastmere Reading House
Meeting Room
42 Pellow Market Row, Crayford, DA3 7QJ
Mobile: 079 4620 7158
Email: eastmerevelmorictend@brivelmail.net
Like us on Friendwall: Eastmere Velmic Tending
6) Rediation on Quiet Rivers is one of the most powerful mediation tools for spiritual development. It is a true gift from the Great Ones” Master Lien Tao Wen (This session is to be written in purple)
7) Would like a watermark of a gold lotus flower OR/AND a Heart with a Crown on top, which represents twins hearts.

Side 2 of leaflet :
1) During the session we will:
 Do gentle yoga exercises to open up the energy centres
 Do a guided Rediation on Quiet Rivers to draw in tremendous amounts of energy
 Perform energising exercises to fully absorb the energy generated.

2) We do not charge for the evening but ask for a donation. (This sentence must be in Red)

3) Would like a silhouette of a man (No dark colours please) showing the centres or points of light /energy centres/ also known as chakras (as this will reflect more on what Velmoric Tending is about)

Thank you very much

Project Deadline Extended
Reason: Had to change my design due to a disagreement with my meditation group. Mediation wording and images had to be changed. I have all information. Would like to extend deadline until Sunday07th June 2015 if possible. Thank you and please advise if there are any further charges. Once again my sincere apologises.

Target Market(s)

Everyone interested in spirituality/meditation

Font styles to use
Decorative
Other font styles liked:
• ARIAL

Colors
0455a3
ffc214
6b449b
ffffff

Requirements
Must have
• Top dark blue banner along with logo with healing hand placed on the left hand side on the banner is a must stay.
Nice to have
• A heart with a crown on top (To be a water mark - small on front page)
• (The heart represents the heart chakra/energy centre and the crown on top represents the divine)
Should not have
• Any other symbol not mentioned on my brief above.

```html
<!DOCTYPE html>
<html lang="en">
<head>
<meta charset="utf-8">
<title>Reflection on Quiet Rivers – Flyer</title>
<link rel="stylesheet" href="https://fonts.googleapis.com/css2?family=Caladea:ital,wght@0,400;0,700;1,400;1,700&family=Great+Vibes&display=swap">
<style>
  :root {
    --navy: #252a73;
    --royal: #1b3a9c;
    --gold: #e6b23a;
    --gold-line: #c98d1f;
    --orange: #f7a21b;
    --yellow: #ffc214;
    --red: #d4111b;
    --purple: #7b2a86;
    --text-navy: #1d2a6b;
    --page: #ffffff;
    --card-shadow: rgba(0,0,0,0.28);
  }
  * { box-sizing: border-box; margin: 0; padding: 0; }
  html, body { width: 1200px; height: 1000px; overflow: hidden; background: var(--page); }
  body { position: relative; font-family: 'Caladea', serif; color: var(--text-navy); }

  .flyer-side {
    position: absolute; left: 260px; width: 680px; height: 476px;
    background: #fff; overflow: hidden;
    box-shadow: 0 1px 4px var(--card-shadow);
  }
  .flyer-side--front { top: 12px; }
  .flyer-side--back { top: 505px; height: 480px; background: linear-gradient(#fff 0%, #fff 55%, #e9eef3 100%); }

  .shape-layer { position: absolute; inset: 0; width: 100%; height: 100%; }

  .top-banner { position: absolute; left: 0; top: 0; width: 680px; height: 92px; background: var(--navy); }
  .gold-rule { position: absolute; left: 0; top: 92px; width: 680px; height: 4px; background: linear-gradient(90deg, var(--gold-line), var(--gold), var(--gold-line)); }
  .healing-hand {
    position: absolute; left: 0; top: 0; width: 110px; height: 92px;
    background: radial-gradient(circle at 42% 45%, #ffe9a0 0%, #6fc3ff 22%, #2a63d9 45%, #141b4d 75%, var(--navy) 100%);
  }
  .brand-name {
    position: absolute; right: 22px; top: 22px; text-align: right;
    color: var(--gold); font-weight: 700; line-height: 1;
  }
  .brand-name .brand-line1 { display: block; font-size: 31px; letter-spacing: 1px; }
  .brand-name .brand-line2 { display: block; font-size: 22px; margin-top: 4px; }

  .event-title {
    position: absolute; left: 0; width: 680px; top: 104px; text-align: center;
    font-size: 35px; font-weight: 700; color: var(--royal); letter-spacing: 0.3px;
  }

  .twin-hearts {
    position: absolute; left: 20px; top: 153px; width: 98px; height: 72px;
    background: radial-gradient(circle at 40% 40%, #ff5b5b, #c40d14 70%);
    border-radius: 40% 40% 50% 50%;
  }
  .chakra-badge {
    position: absolute; width: 34px; height: 34px; border-radius: 50%;
    background: radial-gradient(circle, #f9d37a, #d9771c 70%);
  }

  .benefits {
    position: absolute; left: 268px; width: 400px; top: 160px; text-align: center;
    color: var(--red); font-weight: 700; font-size: 17px; line-height: 21px;
  }
  .schedule {
    position: absolute; left: 0; width: 680px; top: 218px; text-align: center;
    font-weight: 700; font-size: 18.5px; line-height: 22px; color: var(--text-navy);
  }
  .intro {
    position: absolute; left: 22px; width: 636px; top: 274px; text-align: center;
    font-size: 15px; line-height: 20px;
  }
  .intro .highlight { color: #c58d12; }

  .venue { position: absolute; left: 78px; top: 328px; font-weight: 700; font-size: 15px; line-height: 17px; }
  .venue .venue-label { font-size: 17px; display: block; margin-bottom: 1px; }

  .email { position: absolute; left: 58px; top: 420px; display: flex; align-items: center; gap: 6px; font-size: 12px; }
  .email svg { width: 16px; height: 12px; }

  .lotus-mark {
    position: absolute; left: 285px; top: 320px; width: 95px; height: 72px;
    background: radial-gradient(ellipse at 50% 45%, #ffd24a 0%, #f5a315 55%, rgba(255,255,255,0) 72%);
  }

  .social { position: absolute; left: 473px; top: 329px; display: flex; gap: 5px; font-weight: 700; font-size: 13px; line-height: 15px; }
  .social-square { width: 18px; height: 18px; background: var(--royal); margin-top: 6px; }

  .master-quote {
    position: absolute; left: 362px; top: 387px; width: 300px;
    color: var(--purple); font-style: italic; font-weight: 700; font-size: 11px; line-height: 16px;
  }
  .master-signature {
    position: absolute; right: 18px; top: 452px; font-family: 'Great Vibes', cursive;
    color: var(--purple); font-size: 15px;
  }

  .session-heading {
    position: absolute; left: 0; width: 680px; top: 222px; text-align: center;
    font-weight: 700; font-size: 17px; color: var(--text-navy);
  }
  .session-list { position: absolute; left: 58px; top: 250px; width: 460px; list-style: none; font-size: 15px; line-height: 21px; }
  .session-list li { padding-left: 11px; text-indent: -11px; }
  .session-list li::before { content: "• "; }

  .chakra-figure {
    position: absolute; left: 480px; top: 150px; width: 195px; height: 210px;
    background: radial-gradient(ellipse at 50% 55%, #cfeee6 0%, #b5dfe0 40%, rgba(230,240,245,0) 72%);
  }
  .donation {
    position: absolute; left: 0; width: 630px; top: 360px; text-align: center;
    color: var(--red); font-weight: 700; font-size: 14px;
  }
  .lotus-water {
    position: absolute; left: 0; top: 392px; width: 680px; height: 88px;
    background: linear-gradient(90deg, #f3b3ad, #f6cfa3, #f4e7a6, #c9e6b4, #b7e2e6, #b7c3ea, #d3bde9);
    opacity: 0.75;
  }
</style>
</head>
<body>

<!-- Front side -->
<section class="flyer-side flyer-side--front">
  <svg class="shape-layer" viewBox="0 0 680 476" aria-hidden="true">
    <defs>
      <linearGradient id="band-front" x1="0" y1="0" x2="0" y2="1">
        <stop offset="0" stop-color="#ffc214"/>
        <stop offset="1" stop-color="#f7a21b"/>
      </linearGradient>
    </defs>
    <path d="M0 96 H680 V150 C560 172 420 160 280 166 C150 172 70 192 0 218 Z" fill="url(#band-front)"/>
    <path d="M0 406 C150 438 300 440 420 410 C520 386 600 376 680 372 V476 H0 Z" fill="url(#band-front)"/>
    <path d="M0 428 C160 452 310 452 430 424 C530 400 610 392 680 390" fill="none" stroke="#ffffff" stroke-width="3" opacity="0.8"/>
  </svg>

  <div class="top-banner"></div>
  <div class="healing-hand" role="img" aria-label="Healing hand radiating blue light"></div>
  <div class="brand-name"><span class="brand-line1">VELMORIC TENDING</span><span class="brand-line2">CRAYFORD</span></div>
  <div class="gold-rule"></div>

  <h1 class="event-title">REFLECTION ON QUIET RIVERS</h1>
  <div class="twin-hearts" role="img" aria-label="Two red hearts"></div>
  <div class="chakra-badge" role="img" aria-label="Heart chakra emblem" style="left:82px;top:150px;"></div>

  <p class="benefits">Flush out Stress • Boost Energy<br>Increase Physical &amp; Mental Health • Stay Focused</p>

  <p class="schedule">Every First and Third Friday of the month<br>19:45pm – 20:45pm Recurring Event</p>

  <p class="intro">Our guided Mediation is for over 18’s only. <span class="highlight">Reflection on Quiet Rivers</span> is one of the most powerful meditations, practiced worldwide as a global healing technique.</p>

  <div class="venue">
    <span class="venue-label">Where:</span>
    Eastmere Reading House<br>
    Meeting Room<br>
    42 Pellow Market Row,<br>
    Crayford, DA3 7QJ
  </div>

  <div class="email">
    <svg viewBox="0 0 16 12" aria-hidden="true"><rect x="0.5" y="0.5" width="15" height="11" rx="1" fill="#f5c35a" stroke="#c98d1f"/><path d="M1 1 L8 7 L15 1" fill="none" stroke="#c98d1f"/></svg>
    <span>eastmerevelmorictend@brivelmail.net</span>
  </div>

  <div class="lotus-mark" role="img" aria-label="Golden lotus flower"></div>

  <div class="social">
    <span class="social-square"></span>
    <span>Like us on Friendwall:<br>Eastmere Velmic Tending</span>
  </div>

  <div class="chakra-badge" role="img" aria-label="Heart chakra emblem" style="left:322px;top:410px;"></div>
  <p class="master-quote">«Rediation on Quiet Rivers is one of the most powerful mediation tools for spiritual development. It is true gift from the Great Ones»</p>
  <p class="master-signature">Master Lien Tao Wen</p>
</section>

<!-- Back side -->
<section class="flyer-side flyer-side--back">
  <svg class="shape-layer" viewBox="0 0 680 480" aria-hidden="true">
    <defs>
      <linearGradient id="band-back" x1="0" y1="0" x2="0" y2="1">
        <stop offset="0" stop-color="#ffc214"/>
        <stop offset="1" stop-color="#f7a21b"/>
      </linearGradient>
    </defs>
    <path d="M0 96 H680 V186 C600 160 500 148 380 152 C240 156 110 176 0 220 Z" fill="url(#band-back)"/>
  </svg>

  <div class="top-banner"></div>
  <div class="healing-hand" role="img" aria-label="Healing hand radiating blue light"></div>
  <div class="brand-name"><span class="brand-line1">VELMORIC TENDING</span><span class="brand-line2">CRAYFORD</span></div>
  <div class="gold-rule"></div>

  <h1 class="event-title">REFLECTION ON QUIET RIVERS</h1>
  <div class="twin-hearts" role="img" aria-label="Two red hearts"></div>
  <div class="chakra-badge" role="img" aria-label="Heart chakra emblem" style="left:82px;top:150px;"></div>

  <div class="chakra-figure" role="img" aria-label="Light seated meditating figure showing the seven chakras"></div>

  <h2 class="session-heading">DURING THE SESSION WE WILL:</h2>
  <ul class="session-list">
    <li>Do gentle yoga exercises to open up the energy centres</li>
    <li>Do a guided Rediation on Quiet Rivers to draw in tremendous amounts of energy</li>
    <li>Perform energizing exercises to fully absorb the energy generated</li>
  </ul>

  <p class="donation">We do not charge for the evening but ask for a donation.</p>

  <div class="lotus-water" role="img" aria-label="Row of seven rainbow-coloured lotus flowers on calm water"></div>
</section>

</body>
</html>
```